Bellmoor Health Standing Banner

Design a standing banner for a community health care clinic. Our website is www.bellmoorhealth.org. On there you can find our list of services. I have uploaded our logo, mission/vision/about us statements, as well as our business cards for contact information and so you have an idea of the theme we are going for.
Our tagline is building a healthier society.

We want the banner to showcase our name, tagline, services, and the contact methods listed on the business card except for the address.

```html
<!DOCTYPE html>
<html lang="en">
<head>
<meta charset="utf-8">
<title>Bellmoor Health Standing Banner</title>
<link href="https://fonts.googleapis.com/css2?family=Lato:wght@300;400;700;900&family=Parisienne&display=swap" rel="stylesheet">
<style>
  :root {
    --page-bg: #e6e6e6;
    --brand-green: #63b03d;
    --charcoal: #3a3a3a;
    --ink: #2f2f2f;
    --white: #ffffff;
    --accent-orange: #ef5a26;
    --photo-light: #c9c9cc;
    --photo-dark: #6f7074;
  }
  html, body {
    margin: 0;
    padding: 0;
    width: 1200px;
    height: 1044px;
    overflow: hidden;
    background: var(--page-bg);
    font-family: "Lato", Arial, sans-serif;
  }
  .stage {
    position: relative;
    width: 1200px;
    height: 1044px;
  }
  .banner {
    position: absolute;
    left: 397px;
    top: 22px;
    width: 527px;
    height: 1295px;
    transform: scale(0.772);
    transform-origin: top left;
    background: var(--white);
    overflow: hidden;
  }
  .banner-shapes {
    position: absolute;
    inset: 0;
    width: 527px;
    height: 1295px;
  }
  .headline {
    position: absolute;
    left: 32px;
    top: 528px;
    margin: 0;
    line-height: 1;
  }
  .headline-lead {
    display: block;
    font-weight: 300;
    font-size: 38px;
    color: var(--ink);
    letter-spacing: -0.5px;
  }
  .headline-main {
    display: block;
    font-weight: 900;
    font-size: 62px;
    line-height: 0.98;
    color: var(--white);
    letter-spacing: -1px;
    margin-top: 4px;
  }
  .services-title {
    position: absolute;
    left: 38px;
    top: 750px;
    margin: 0;
    font-size: 21px;
    font-weight: 700;
    color: var(--ink);
    text-decoration: underline;
    text-underline-offset: 3px;
    letter-spacing: -0.3px;
  }
  .services-list {
    position: absolute;
    left: 38px;
    top: 796px;
    width: 480px;
    margin: 0;
    padding: 0;
    list-style: none;
    display: grid;
    grid-template-columns: 195px 1fr;
    row-gap: 18px;
  }
  .services-list li {
    font-size: 28px;
    font-weight: 400;
    color: var(--white);
    line-height: 34px;
    letter-spacing: -0.3px;
  }
  .services-list li::before {
    content: "•";
    color: var(--ink);
    margin-right: 6px;
    font-size: 24px;
  }
  .brand-mark {
    position: absolute;
    left: 366px;
    top: 1032px;
    width: 84px;
    height: 84px;
    border-radius: 50%;
    background: var(--accent-orange);
  }
  .brand-name {
    position: absolute;
    right: 21px;
    top: 1128px;
    margin: 0;
    font-size: 40px;
    font-weight: 400;
    color: var(--brand-green);
    line-height: 1;
  }
  .brand-tagline {
    position: absolute;
    right: 22px;
    top: 1176px;
    margin: 0;
    font-family: "Parisienne", cursive;
    font-size: 20px;
    color: var(--brand-green);
  }
  .contact-line {
    position: absolute;
    right: 21px;
    top: 1228px;
    margin: 0;
    display: flex;
    align-items: center;
    gap: 8px;
    font-size: 18px;
    color: var(--white);
  }
  .contact-item {
    display: inline-flex;
    align-items: center;
    gap: 6px;
  }
  .contact-item + .contact-item { margin-left: 10px; }
  .contact-icon { width: 18px; height: 14px; }
  .website {
    position: absolute;
    right: 21px;
    top: 1256px;
    margin: 0;
    font-size: 16px;
    font-weight: 700;
    letter-spacing: 5.5px;
    color: var(--white);
  }
</style>
</head>
<body>
<main class="stage">
  <section class="banner">
    <svg class="banner-shapes" viewBox="0 0 527 1295" xmlns="http://www.w3.org/2000/svg">
      <defs>
        <linearGradient id="photoTone" x1="0" y1="0" x2="1" y2="1">
          <stop offset="0" stop-color="var(--photo-light)"/>
          <stop offset="0.55" stop-color="#e4e4ea"/>
          <stop offset="1" stop-color="var(--photo-dark)"/>
        </linearGradient>
      </defs>
      <polygon class="hero-photo" role="img" aria-label="Photo of a lab scientist in a hairnet and white coat looking into a microscope" points="0,0 527,0 527,606 0,386" fill="url(#photoTone)"/>
      <polygon class="green-panel" points="0,425 527,612 527,956 0,1138" fill="var(--brand-green)"/>
      <polygon class="footer-panel" points="0,1177 527,960 527,1295 0,1295" fill="var(--charcoal)"/>
    </svg>

    <h1 class="headline">
      <span class="headline-lead">BUILDING A</span>
      <span class="headline-main">HEALTHIER<br>SOCIETY</span>
    </h1>

    <h2 class="services-title">OUR SERVICES:</h2>
    <ul class="services-list">
      <li>Lab</li>
      <li>Community Clinic</li>
      <li>Nutrition</li>
      <li>Substance Abuse</li>
      <li>Health Fairs</li>
      <li>Clinical Research</li>
    </ul>

    <span class="brand-mark" aria-hidden="true"></span>
    <p class="brand-name">Bellmoor Health</p>
    <p class="brand-tagline">Building a healthier society</p>

    <p class="contact-line">
      <span class="contact-item">
        <svg class="contact-icon" viewBox="0 0 18 14" aria-hidden="true"><path d="M1 5 Q9 -1 17 5 L15 7 L12 5 L12 3.5 Q9 2.5 6 3.5 L6 5 L3 7 Z M5 7 H13 L15 13 H3 Z" fill="var(--brand-green)"/></svg>
        555-014-2290
      </span>
      <span class="contact-item">
        <svg class="contact-icon" viewBox="0 0 18 14" aria-hidden="true"><rect x="1" y="1" width="16" height="12" fill="var(--brand-green)"/><path d="M1.5 1.5 L9 8 L16.5 1.5" stroke="var(--charcoal)" stroke-width="1.4" fill="none"/></svg>
        info@bellmoorhealth.org
      </span>
    </p>
    <p class="website">www.bellmoorhealth.org</p>
  </section>
</main>
</body>
</html>
```